Flyer "Pinch Analysis"-Energy Optimization procedure for Industry

We need a flyer (1xA4 recto/verso )design for a new part of our business.

In Summary: we want to communicate that we are providing "Pinch Analysis" for the industry. It's an energy optimization procedure. We are a cutting edge engineering consulting group.

All details about project in the attached files

Target Market(s)

Engineering

Industry/Entity Type

Business

Font styles to use
Serif

Requirements
Must have
• Finale document in .ai format ready for printing
• More informations in attached files
Nice to have
• See attached files

```html
<!DOCTYPE html>
<html lang="fr">
<head>
<meta charset="utf-8">
<title>Analyse Pinch – Kovara Engineering</title>
<link href="https://fonts.googleapis.com/css2?family=Arimo:wght@400;700&display=swap" rel="stylesheet">
<style>
:root{
  --stage:#d9d6d2;
  --page:#050505;
  --white:#ffffff;
  --sky:#3bb8e8;
  --steel-dark:#2b2b2b;
  --steel-light:#b9bcbf;
  --blue-tank:#2c6fa8;
  --red-curve:#e8232a;
  --blue-curve:#2e3192;
  --grey-text:#c9c9c9;
}
*{margin:0;padding:0;box-sizing:border-box}
html,body{width:1200px;height:1000px;overflow:hidden;background:var(--stage);font-family:"Arimo",sans-serif}
.canvas{position:relative;width:1200px;height:1000px}
.page{position:absolute;left:259px;width:676px;background:var(--page);overflow:hidden}
.page--front{top:14px;height:477px}
.page--back{top:505px;height:485px}
.brand{position:absolute;display:flex;align-items:center;gap:7px;color:var(--sky);font-weight:700}
.brand__mark{width:10px;height:10px;background:var(--sky)}
.front-brand{left:22px;top:34px;font-size:19px}
.back-brand{left:12px;top:374px;font-size:15px}
.front-photo{position:absolute;right:0;top:0;width:440px;height:477px}
.front-title{position:absolute;left:24px;top:122px;width:240px;color:var(--white);font-weight:700;font-size:18.5px;line-height:25px}
.chart{position:absolute;left:0;top:320px}
.back-header{position:absolute;left:11px;top:25px;width:500px;height:45px;background:var(--sky);color:var(--white);font-weight:700;font-size:14.5px;line-height:18px;padding:4px 0 0 13px}
.back-body{position:absolute;left:12px;top:86px;width:384px;color:var(--white);font-size:7.4px;line-height:9.6px}
.back-body p{text-indent:12px;margin-bottom:9.6px}
.back-body ul{list-style:none;margin:-9.6px 0 9.6px 0;padding-left:12px}
.back-body li::before{content:"•"}
.back-photos{position:absolute;right:0;top:0}
.contact-band{position:absolute;left:11px;top:402px;width:420px;height:18px;background:var(--sky);color:var(--white);font-size:13px;line-height:18px;padding-left:12px}
.contact-info{position:absolute;left:12px;top:432px;color:var(--grey-text);font-size:7.4px;line-height:9.6px}
</style>
</head>
<body>
<div class="canvas">

  <section class="page page--front">
    <svg class="front-photo" width="440" height="477" role="img" aria-label="Photo en noir et blanc d'un réseau de tuyauteries industrielles">
      <defs>
        <linearGradient id="steelFade" x1="0" x2="1" y1="0" y2="0">
          <stop offset="0" stop-color="#050505"/>
          <stop offset="0.18" stop-color="#3a3a3a"/>
          <stop offset="0.6" stop-color="#8e9194"/>
          <stop offset="1" stop-color="#5d6063"/>
        </linearGradient>
      </defs>
      <rect width="440" height="477" fill="url(#steelFade)"/>
    </svg>

    <div class="brand front-brand"><span class="brand__mark"></span>Kovara Engineering</div>

    <h1 class="front-title">Analyse Pinch – en route vers la performance opérationnelle et l’efficacité énergétique</h1>

    <svg class="chart" width="280" height="157" aria-label="Courbes composites : température en fonction du flux de chaleur">
      <g font-family="Arimo, sans-serif" font-size="4.5" fill="#bbbbbb">
        <line x1="26" y1="20" x2="26" y2="142" stroke="#bbbbbb" stroke-width="0.6"/>
        <line x1="26" y1="142" x2="264" y2="142" stroke="#bbbbbb" stroke-width="0.6"/>
        <text x="12" y="24">140</text><text x="12" y="42">120</text><text x="12" y="59">100</text>
        <text x="14" y="77">80</text><text x="14" y="94">60</text><text x="14" y="112">40</text><text x="14" y="129">20</text>
        <text x="25" y="150">0</text><text x="53" y="150">100</text><text x="82" y="150">200</text><text x="112" y="150">300</text>
        <text x="141" y="150">400</text><text x="171" y="150">500</text><text x="200" y="150">600</text><text x="229" y="150">700</text><text x="258" y="150">800</text>
        <text x="184" y="137" font-weight="700">Heat Flow (kW)</text>
        <text transform="translate(34,70) rotate(-90)" font-weight="700">Actual Temperature °C</text>
      </g>
      <polyline points="26,141 59,132 103,112 103,92" fill="none" stroke="var(--red-curve)" stroke-width="2"/>
      <polyline points="46,145 141,102 154,33 244,33" fill="none" stroke="var(--blue-curve)" stroke-width="2"/>
    </svg>
  </section>

  <section class="page page--back">
    <svg class="back-photos" width="676" height="485" viewBox="0 0 676 485">
      <path d="M520,0 L676,0 L676,210 Q520,220 450,300 Q430,120 520,0 Z" fill="#c7c8c8" role="img" aria-label="Photo d'une salle technique avec cuves et tuyauteries"/>
      <circle cx="590" cy="375" r="170" fill="var(--blue-tank)" role="img" aria-label="Photo d'une installation industrielle avec réservoirs bleus et conduites"/>
      <path d="M520,0 Q430,120 450,300" fill="none" stroke="var(--sky)" stroke-width="3"/>
      <circle cx="590" cy="375" r="170" fill="none" stroke="var(--sky)" stroke-width="3"/>
    </svg>

    <h2 class="back-header">Analyse Pinch – en route vers la performance opérationnelle et l’efficacité énergétique</h2>

    <div class="back-body">
      <p>La performance opérationnelle et l’efficacité énergétique sont les clés de la réussite de l’industrie de demain.</p>
      <p>Fort d’une longue expérience dans l’analyse, la conception et la mise en service d’installations industrielles (chimie, alimentaire, pharmacie,…), la société Kovara utilise l’analyse Pinch dans sa démarche de conception et d’amélioration.</p>
      <p>L’analyse Pinch est une méthode d’analyse systématique développée et appliquée depuis les années 1980; elle permet de répondre aux questions suivantes:</p>
      <ul>
        <li>Quels sont les besoins de chaleur et de froid minimaux de mon procédé</li>
        <li>Quel est mon potentiel de réduction de consommation énergétique</li>
        <li>Quel est la solution technique présentant les coûts minimaux entre investissements et économies</li>
      </ul>
      <p>L’amélioration de l’efficacité énergétique est liée directement à l’exploitation des potentiels de récupération du procédé. Des potentiels de diminution de la consommation de 10 à 30% sont usuels. Nous pouvons également améliorer les performances opérationnelles en analysant vos méthodes de fabrication.</p>
      <p>L’analyse Pinch est aussi bien adaptée pour les PME que pour les grandes entreprises dont les procédés sont exploités de manière continue ou discontinue (batch).</p>
      <p>Etant donné les objectifs énergétiques de la confédération, l’agence nationale de l’énergie (ANE) soutient les analyses Pinch à hauteur de 35% pour les procédés continus et de 60% pour les procédés discontinus (batch).</p>
      <p>Pour tous compléments d’informations et pour savoir si une analyse Pinch est justifiée dans votre cas, nous vous conseillons avec plaisir.</p>
    </div>

    <div class="brand back-brand"><span class="brand__mark"></span>Kovara Engineering</div>

    <div class="contact-band">Contact:</div>
    <address class="contact-info" style="font-style:normal">
      Lucien Marchand, Élise Dufaux<br>
      Kovara SA<br>
      Rue des Vergers 14<br>
      CH-1870 Valmont
    </address>
  </section>

</div>
</body>
</html>
```